Motion Nest Business Cards

Can all designers please apply the following info on their designs' back-side of the business card: (please see brief file upload ('Info for backside...' - for required info, colours & layout)

SPECIALISING IN INDIVIDUAL PILATES INSTRUCTION
MATWORK – including small apparatus
and STUDIO:
VIVANTE 3 GLIDER
LADDER BARREL
COUNTOUR BARREL
FLEXI DOME
VIM STOOL
KIM-O-LAN

Business Cards for Motion Nest - applying the Motion Nest logo design selected earlier.
Note the business card requires both a front and back side. Please refer to two uploaded ppt-files for type of info required to be displayed, and rough position of where info could be. Require innovative / fresh approach to business card design and use of colour by designers now. Please refer to and use logo as uploaded - also for potential business card colour application.

Dear Designers,

Please note the additional inclusion / upload of two draft ppt-files that try to show where I want what type of information, for both the front & back sides of the required business card, plus an attempt at showing the high-level concept / idea of business info position.

As my 'drafts' obviously lack colour and any ability towards innovative card design or approach – I now rely on your vastly superior graphic design abilities to produce a really great business card for my business…

Looking forward to your submissions!

Kind regards, Merika for: Motion Nest 

Hello all Designers,

Can all designers please apply the following info on their designs' back-side of the business card: (please see / refer to the Brief and specifically the file upload ('Info for backside...' - for required info, colours & layout) - for the backside of the business card).

Info content (without colour, layout etc.):

and STUDIO:

VIVANTE 3 GLIDER

LADDER BARREL

COUNTOUR BARREL

FLEXI DOME

VIM STOOL

KIM-O-LAN

Thank you to all designers that submitted for consideration!

With regards,

Motion Nest

```html
<!DOCTYPE html>
<html lang="en">
<head>
<meta charset="utf-8">
<title>Motion Nest Business Cards</title>
<link rel="stylesheet" href="https://fonts.googleapis.com/css2?family=Open+Sans:ital,wght@0,400;0,700;1,400&family=Architects+Daughter&display=swap">
<style>
  :root {
    --backdrop: #d6d6d6;
    --card: #ffffff;
    --orange: #e05010;
    --leaf-dark: #445f04;
    --leaf-light: #a6d96a;
    --ink: #3a3a3a;
  }
  * { margin: 0; padding: 0; box-sizing: border-box; }
  html, body { width: 1200px; height: 1000px; overflow: hidden; }
  body {
    background: var(--backdrop);
    font-family: "Open Sans", Arial, sans-serif;
    color: var(--ink);
    position: relative;
  }
  .card {
    position: absolute;
    top: 303px;
    width: 573px;
    height: 328px;
    background: var(--card);
    overflow: hidden;
  }
  .card--front { left: 22px; }
  .card--back { left: 606px; }

  .card__band {
    position: absolute;
    left: 0;
    width: 573px;
    bottom: 0;
  }
  .card--front .card__band {
    top: 232px;
    background: linear-gradient(180deg, var(--leaf-dark) 0%, var(--leaf-dark) 38%, var(--leaf-light) 70%, var(--orange) 100%);
  }
  .card--back .card__band {
    top: 248px;
    background: linear-gradient(180deg, var(--leaf-light) 0%, var(--leaf-dark) 25%, var(--leaf-dark) 45%, var(--orange) 100%);
  }

  .t { position: absolute; line-height: 1; white-space: nowrap; }

  .brand { left: 92px; top: 38px; display: flex; align-items: center; gap: 16px; }
  .brand__dot { width: 42px; height: 42px; border-radius: 50%; background: var(--leaf-dark); }
  .brand__name { font-size: 46px; font-weight: 400; color: var(--orange); line-height: 1; }

  .holder__name { left: 0; width: 573px; text-align: center; top: 95px; font-size: 21px; font-weight: 700; }
  .holder__title { left: 0; width: 573px; text-align: center; top: 119px; font-size: 15px; font-style: italic; }

  .contact { font-size: 16.5px; }
  .label { color: var(--orange); }
  .tagline {
    left: 118px; top: 241px; font-family: "Architects Daughter", cursive;
    font-size: 15px; letter-spacing: 2px; color: #fff;
  }
  .tagline .sep { color: var(--orange); margin: 0 9px; font-size: 18px; }

  .back__head { left: 0; width: 573px; text-align: center; top: 59px; font-size: 16.5px; font-weight: 700; color: var(--orange); }
  .back__mat { left: 0; width: 573px; text-align: center; top: 95px; font-size: 16px; }
  .back__studio { left: 0; width: 573px; text-align: center; top: 125px; font-size: 16px; font-weight: 700; }
  .kit { position: absolute; list-style: none; font-size: 16px; line-height: 18px; }
  .kit li::before { content: "\2022"; color: var(--orange); margin-right: 5px; font-size: 19px; }
  .kit--a { left: 96px; top: 154px; }
  .kit--b { left: 334px; top: 154px; }
</style>
</head>
<body>

<section class="card card--front">
  <div class="card__band" role="img" aria-label="Decorative flowing bands in dark green, light green and orange"></div>

  <div class="t brand"><span class="brand__dot"></span><span class="brand__name">Motion Nest</span></div>
  <div class="t holder__name">Merika Halvorsen</div>
  <div class="t holder__title">Diploma of Professional Pilates Instruction</div>

  <div class="t contact label" style="left:51px;top:149px;">Studio Location:</div>
  <div class="t contact" style="left:51px;top:172px;">18 Linden Crescent</div>
  <div class="t contact" style="left:51px;top:195px;">Brookhaven WA 6090</div>

  <div class="t contact" style="left:295px;top:149px;"><span class="label">M:</span> 041 000 1234</div>
  <div class="t contact" style="left:295px;top:172px;"><span class="label">E:</span>&nbsp;&nbsp; info@motionnest.com</div>
  <div class="t contact" style="left:295px;top:195px;"><span class="label">W:</span> www.motionnest.com.au</div>

  <div class="t tagline">BALANCE<span class="sep">&bull;</span>STRENGTH<span class="sep">&bull;</span>FLEXIBILITY</div>
</section>

<section class="card card--back">
  <div class="card__band" role="img" aria-label="Decorative flowing bands in green and orange"></div>

  <div class="t back__head">Specialising in Indiviudal Pilates Instruction</div>
  <div class="t back__mat"><strong>MATWORK</strong> (including Small Apparatus)</div>
  <div class="t back__studio">STUDIO:</div>
  <ul class="kit kit--a">
    <li>VIVANTE 3 GLIDER</li>
    <li>LADDER BARREL</li>
    <li>COUNTOUR BARREL</li>
  </ul>
  <ul class="kit kit--b">
    <li>FLEXI DOME</li>
    <li>VIM STOOL</li>
    <li>KIM-O-LAN</li>
  </ul>
</section>

</body>
</html>
```